Design refresh of existing HR Application

QuillStaff is an HR & Payroll processing software, already in use by thousands of people. It is a feature packed, enterprise-grade software that is also simple and user friendly. Visit us at https://quillstaff.example

Seeking a refresh of the app design/UI.

Key objectives are to make it "sleeker", more professional and polished, whist still retaining functionality. Not intended to be a massive overhaul, but more of reorganization and improvements on design elements.

You may login to our demo account to see the app live.
https://app.quillstaff.example/login
User: demo@quillstaff.example
Password: Zip20

Target Market(s)

HR Managers, business administrators/owners and employees.

Industry/Entity Type

Business Software

Number of Pages Required

4 page

Font styles to use
Other font styles liked:
• Lato

Colors
0255a3
3377b5
00a990
33b8a4
f37122
faa54b

Requirements
Must have
• Must retain the current functionality on each page.
Nice to have
• Fine to suggest changes to colors, font sizes, card designs, moving sections around and any other design element changes.

```html
<!DOCTYPE html>
<html lang="en">
<head>
<meta charset="utf-8">
<title>Leave Request</title>
<link href="https://fonts.googleapis.com/css2?family=DM+Sans:wght@400;500;700&display=swap" rel="stylesheet">
<style>
  :root{
    --stage:#c2fff7;
    --primary:#0255a3;
    --primary-mid:#3377b5;
    --ink:#2c2f3a;
    --ink-soft:#5b5f6b;
    --muted:#9a9ea8;
    --border:#dcdfe6;
    --profile-bg:#e5e9f2;
    --day-head:#eaf4fd;
    --month-col:#f7ebfc;
    --cell:#f7f7f8;
    --grid-line:#e4e5ee;
    --btn-disabled:#dcdcdc;
    --white:#ffffff;
  }
  *{box-sizing:border-box;margin:0;padding:0}
  html,body{width:1200px;height:1200px;overflow:hidden}
  body{background:var(--stage);font-family:"DM Sans",Arial,sans-serif;color:var(--ink);position:relative}

  .leave-modal{position:absolute;left:50px;top:141px;width:1100px;background:var(--white);box-shadow:0 10px 40px rgba(0,60,80,.12)}
  .modal-top{display:flex;height:391px}

  .profile-card{width:361px;background:var(--profile-bg);display:flex;flex-direction:column;align-items:center;padding-top:47px}
  .profile-photo{width:150px;height:150px;border-radius:50%;background:radial-gradient(circle at 50% 40%,#8a8a8a,#3c3c3c 70%)}
  .profile-name{margin-top:14px;font-size:20px;font-weight:500;color:var(--primary)}
  .profile-role{margin-top:4px;font-size:14px;color:var(--ink)}
  .profile-dept{margin-top:5px;font-size:11px;color:var(--ink-soft)}
  .profile-contacts{margin-top:20px;display:grid;grid-template-columns:170px 100px;row-gap:16px;column-gap:0}
  .contact{display:flex;align-items:center;gap:8px;font-size:11.5px;color:var(--primary)}
  .contact svg{width:20px;height:20px;flex:none}

  .request-form{flex:1;padding:28px 36px 0 36px;position:relative}
  .form-title{font-size:18px;font-weight:500;color:var(--ink)}
  .field-row{display:flex;margin-top:30px}
  .field label,.attach-label{display:block;font-size:14px;color:var(--ink);margin-bottom:7px}
  .input{height:47px;border:1px solid var(--border);border-radius:2px;display:flex;align-items:center;justify-content:space-between;padding:0 14px;font-size:14px;color:var(--muted)}
  .input svg{width:18px;height:18px}
  .field-duration{width:217px}
  .field-date{width:186px;margin-left:27px}
  .field-type{width:186px;margin-left:28px}
  .attach-label{margin-top:30px}
  .attach-box{width:645px;height:70px;border:1px solid var(--border);border-radius:2px;display:flex;align-items:center;padding-left:20px;gap:12px}
  .attach-icon{width:38px;height:38px;border-radius:3px;background:var(--primary-mid);display:flex;align-items:center;justify-content:center}
  .attach-hint{font-size:13px;line-height:18px;color:var(--muted)}
  .actions{position:absolute;top:311px;left:355px;display:flex;gap:18px}
  .btn{width:153px;height:49px;border-radius:2px;font-size:17px;font-weight:500;color:var(--white);display:flex;align-items:center;justify-content:center}
  .btn-add{background:var(--btn-disabled)}
  .btn-submit{background:var(--primary)}

  .leave-calendar{font-size:10px}
  .cal-row{display:flex;height:40.5px}
  .cal-head{height:40px;background:var(--day-head)}
  .cal-corner{width:48px;background:var(--white)}
  .cal-month{width:48px;background:var(--month-col);display:flex;align-items:center;justify-content:center;font-size:12px;color:var(--primary)}
  .cal-days{flex:1;display:grid;grid-template-columns:repeat(31,1fr)}
  .cal-days span{display:flex;align-items:center;justify-content:center;color:var(--primary);font-weight:500;font-size:10px}
  .cal-cells{flex:1;background-color:var(--cell);
    background-image:linear-gradient(to right,var(--grid-line) 1px,transparent 1px),linear-gradient(to bottom,var(--grid-line) 1px,transparent 1px);
    background-size:calc(100% / 31) 100%,100% 100%}
</style>
</head>
<body>
<section class="leave-modal">
  <div class="modal-top">
    <aside class="profile-card">
      <div class="profile-photo" role="img" aria-label="Profile photo of the employee"></div>
      <div class="profile-name">Demo Admin</div>
      <div class="profile-role">HR Administrator</div>
      <div class="profile-dept">Human Resources|Branch D|PT Lumen Shipping</div>
      <div class="profile-contacts">
        <div class="contact">
          <svg viewBox="0 0 24 24" fill="none" stroke="currentColor" stroke-width="1.6"><rect x="2" y="5" width="20" height="14" rx="1.5"/><path d="M3 6l9 7 9-7"/></svg>
          demo@quillstaff.example
        </div>
        <div class="contact">
          <svg viewBox="0 0 24 24" fill="none" stroke="currentColor" stroke-width="1.6"><circle cx="12" cy="8" r="4"/><path d="M4 21c0-4.5 3.6-7 8-7s8 2.5 8 7z"/></svg>
          BG00136
        </div>
        <div class="contact">
          <svg viewBox="0 0 24 24" fill="none" stroke="currentColor" stroke-width="1.6"><path d="M5 3l4 1 1 4-2 2a11 11 0 006 6l2-2 4 1 1 4-2 2C10 21 3 14 3 5z"/><path d="M14 3a7 7 0 017 7M14 7a3 3 0 013 3"/></svg>
          +6280011223344
        </div>
        <div class="contact">
          <svg viewBox="0 0 24 24" fill="none" stroke="currentColor" stroke-width="1.6"><rect x="2" y="5" width="20" height="15" rx="1.5"/><path d="M9 5V3h6v2"/><circle cx="8" cy="11" r="2"/><path d="M5 17c0-2 1.5-3 3-3s3 1 3 3M14 10h5M14 13h5M14 16h4"/></svg>
          1651
        </div>
      </div>
    </aside>

    <div class="request-form">
      <h1 class="form-title">Leave Request</h1>
      <div class="field-row">
        <div class="field field-duration">
          <label>Duration</label>
          <div class="input">Full Day
            <svg viewBox="0 0 24 24" fill="none" stroke="#555" stroke-width="2.2"><path d="M6 9l6 6 6-6"/></svg>
          </div>
        </div>
        <div class="field field-date">
          <label>Start Date</label>
          <div class="input">29 May 2020
            <svg viewBox="0 0 24 24" fill="none" stroke="#3377b5" stroke-width="1.6"><rect x="3" y="4" width="18" height="17"/><path d="M3 9h18M9 9v12M15 9v12M3 15h18M8 2v4M16 2v4"/></svg>
          </div>
        </div>
        <div class="field field-type">
          <label>Leave Type</label>
          <div class="input">Choose leave type
            <svg viewBox="0 0 24 24" fill="none" stroke="#555" stroke-width="2.2"><path d="M6 9l6 6 6-6"/></svg>
          </div>
        </div>
      </div>
      <span class="attach-label">Attachment</span>
      <div class="attach-box">
        <div class="attach-icon">
          <svg width="22" height="22" viewBox="0 0 24 24" fill="none" stroke="#fff" stroke-width="1.7"><path d="M20 11l-8 8a5 5 0 01-7-7l9-9a3.5 3.5 0 015 5l-9 9a2 2 0 01-3-3l8-8"/></svg>
        </div>
        <p class="attach-hint">Attachments (e.g. receipt etc. Max file size: 300KB each.<br>Accepted formats: PDF, JPEG, PNG, GIF)</p>
      </div>
      <div class="actions">
        <div class="btn btn-add">Add</div>
        <div class="btn btn-submit">Submit</div>
      </div>
    </div>
  </div>

  <div class="leave-calendar">
    <div class="cal-row cal-head">
      <div class="cal-corner"></div>
      <div class="cal-days">
        <span>1</span><span>2</span><span>3</span><span>4</span><span>5</span><span>6</span><span>7</span><span>8</span><span>9</span><span>10</span><span>11</span><span>12</span><span>13</span><span>14</span><span>15</span><span>16</span><span>17</span><span>18</span><span>19</span><span>20</span><span>21</span><span>22</span><span>23</span><span>24</span><span>25</span><span>26</span><span>27</span><span>28</span><span>29</span><span>30</span><span>31</span>
      </div>
    </div>
    <div class="cal-row"><div class="cal-month">Jan</div><div class="cal-cells"></div></div>
    <div class="cal-row"><div class="cal-month">Feb</div><div class="cal-cells"></div></div>
    <div class="cal-row"><div class="cal-month">Mar</div><div class="cal-cells"></div></div>
    <div class="cal-row"><div class="cal-month">Apr</div><div class="cal-cells"></div></div>
    <div class="cal-row"><div class="cal-month">May</div><div class="cal-cells"></div></div>
    <div class="cal-row"><div class="cal-month">Jun</div><div class="cal-cells"></div></div>
    <div class="cal-row"><div class="cal-month">Jul</div><div class="cal-cells"></div></div>
    <div class="cal-row"><div class="cal-month">Aug</div><div class="cal-cells"></div></div>
    <div class="cal-row"><div class="cal-month">Sep</div><div class="cal-cells"></div></div>
    <div class="cal-row"><div class="cal-month">Oct</div><div class="cal-cells"></div></div>
    <div class="cal-row"><div class="cal-month">Nov</div><div class="cal-cells"></div></div>
    <div class="cal-row"><div class="cal-month">Dec</div><div class="cal-cells"></div></div>
  </div>
</section>
</body>
</html>
```